Mobile (Android/iPhone) game studio needs stationary design and a business card

We are Plunk Ferret Software and we need a fun and creative stationary design. Our company builds Android and iPhone games and children's software. The stationary designs should reflect an entertainment, fun and creativity. The pieces of stationary we need are:
1. A4 and Letter Word template (company letterhead)
2. A4 and Letter PPT template
3. Business card
4. Envelopes of various standard sizes
Each of the designs should somehow utilize our company logo.
The business card should have the following:
1. Incorporates our company logo (see attached)
2. Has a front and back with the same design (front is English, back is Traditional Chinese)
3. Delivered in an editable template so we can easily add new business cards using the same template when we hire more employees
4. Field for full name
5. Field for employee's title
6. Field for employee's email address
7. Field for company phone number - +886-2-51384470
8. Field for mobile phone number
9. Field for company fax number - +886-2-51384492
10. Company website address: www.plunkferret.example
11. Company address (on English side): 7F-2, NO. 63, Lane 91, Guoyuan Road, Dali District, Taipei Taiwan
12. Company address (on Traditional Chinese side): See Word document attachment for address in Chinese characters
Industry/Entity Type
Games
Look and feel
Each slider illustrates characteristics of the customer's brand and the style your logo design should communicate.

```html
<!DOCTYPE html>
<html lang="en">
<head>
<meta charset="utf-8">
<title>Plunk Ferret Software – Envelope</title>
<link rel="stylesheet" href="https://fonts.googleapis.com/css2?family=Arimo:wght@400;700&display=swap">
<style>
  :root {
    --brand-blue: #0a8fd8;
    --brand-blue-light: #139fe3;
    --brand-blue-dark: #0470b8;
    --paper: #ffffff;
    --paper-edge: #e4e6e8;
    --text-grey: #6d6e70;
    --window-line: #d5d7d9;
    --backdrop: #ffffff;
  }
  * { box-sizing: border-box; margin: 0; padding: 0; }
  html, body {
    width: 1200px;
    height: 910px;
    overflow: hidden;
    background: var(--backdrop);
    font-family: "Arimo", Arial, sans-serif;
  }
  .stage { position: relative; width: 1200px; height: 910px; }

  .envelope {
    position: absolute;
    background: var(--paper);
    border: 1px solid var(--paper-edge);
  }

  /* Reverse side with the folded flap */
  .envelope--back { left: 100px; top: 60px; width: 860px; height: 440px; }
  .envelope__flap { position: absolute; left: 0; top: 0; width: 100%; height: 100%; }

  /* Address side */
  .envelope--front { left: 240px; top: 388px; width: 865px; height: 445px; }

  .band {
    position: absolute;
    top: 40px;
    height: 72px;
    background: linear-gradient(to bottom, var(--brand-blue-light), var(--brand-blue) 55%, var(--brand-blue-dark));
  }
  .band--stub { left: 12px; width: 52px; }
  .band--main { left: 195px; right: 0; }

  .brand {
    position: absolute;
    left: 68px;
    top: 30px;
    width: 124px;
    height: 90px;
    display: flex;
    flex-direction: column;
    align-items: center;
    justify-content: center;
    gap: 6px;
  }
  .brand__dot {
    width: 30px;
    height: 30px;
    border-radius: 50%;
    background: var(--brand-blue);
  }
  .brand__name {
    font-weight: 700;
    font-size: 13px;
    line-height: 1.15;
    color: var(--brand-blue);
    text-align: center;
  }

  .address-window {
    position: absolute;
    left: 632px;
    top: 44px;
    width: 178px;
    height: 86px;
    background: var(--paper);
    border: 1px solid var(--window-line);
    border-radius: 12px;
  }

  .contact {
    position: absolute;
    left: 448px;
    top: 370px;
    padding-left: 19px;
    border-left: 1.5px solid var(--brand-blue);
    font-size: 10.5px;
    line-height: 14px;
    color: var(--text-grey);
    white-space: nowrap;
  }
  .contact__row { display: block; }
  .contact__label { color: var(--brand-blue); }
  .contact__sep { color: var(--brand-blue); margin: 0 12px; }
</style>
</head>
<body>
<main class="stage">

  <section class="envelope envelope--back" aria-label="Envelope reverse with flap">
    <svg class="envelope__flap" viewBox="0 0 860 440" preserveAspectRatio="none" aria-hidden="true">
      <defs>
        <linearGradient id="flapShade" x1="0" y1="0" x2="0" y2="1">
          <stop offset="0" stop-color="#0477c2"/>
          <stop offset="0.55" stop-color="#0d97dd"/>
          <stop offset="1" stop-color="#0a8fd8"/>
        </linearGradient>
      </defs>
      <polygon points="0,0 860,0 445,220" fill="url(#flapShade)"/>
    </svg>
  </section>

  <section class="envelope envelope--front" aria-label="Envelope address side">
    <div class="band band--stub"></div>
    <div class="brand">
      <span class="brand__dot"></span>
      <span class="brand__name">Plunk Ferret<br>Software</span>
    </div>
    <div class="band band--main"></div>
    <div class="address-window"></div>

    <address class="contact" style="font-style:normal">
      <span class="contact__row">
        <span class="contact__label">T:</span> 02 9417 2208
        <span class="contact__sep">|</span>
        <span class="contact__label">F:</span> 02 9417 2209
        <span class="contact__sep">|</span>
        <span class="contact__label">M:</span> 02 9417 6630 2741
      </span>
      <span class="contact__row">
        mira@plunkferret.example
        <span class="contact__sep">|</span>
        www.plunkferret.example
      </span>
      <span class="contact__row">7F-2, NO. 63, Lane 91, Guoyuan Road, Dali District, Taipei Taiwan</span>
    </address>
  </section>

</main>
</body>
</html>
```